Oakmere Kin Clinic

We are a doctors surgery, providing medical services to all ages

we aim for a professional as well as an eye catching look for the signs that can be seen by passing vehicles and people who walk by

trustworthy quality medical care to to all patients, we treat like family

Name- Brenwick Kin Clinic Medical practice

Target Market(s)

all ages, adults
the elderly

Industry/Entity Type

Medical

Requirements
Must have
• eye catching,
obvious medical service location

```html
<!DOCTYPE html>
<html lang="en">
<head>
<meta charset="utf-8">
<title>Brenwick Kin Clinic – Medical Practice Sign</title>
<link rel="stylesheet" href="https://fonts.googleapis.com/css2?family=Montserrat:wght@400;500&family=Bitter:wght@300&display=swap">
<style>
  :root {
    --backdrop: #2c333b;
    --sign-white: #ffffff;
    --sign-grey: #e4e6e9;
    --title-grey: #4a4d51;
    --accent-pink: #ec5fa3;
    --phone-blue: #1b6fb8;
    --band-green: #6cbf45;
    --brand-blue: #1b7fc4;
    --photo-skin: #e8c9b0;
    --photo-blue: #9cc8ea;
    --photo-light: #f3f2f0;
  }
  * { margin: 0; padding: 0; box-sizing: border-box; }
  html, body {
    width: 1200px; height: 750px; overflow: hidden;
    background: var(--backdrop);
  }
  .sign {
    position: absolute; left: 100px; top: 241px;
    width: 1000px; height: 267px; overflow: hidden;
    background: linear-gradient(to bottom, var(--sign-white) 0%, var(--sign-white) 62%, var(--sign-grey) 100%);
    font-family: "Montserrat", sans-serif;
  }
  .hero-photo {
    position: absolute; left: 620px; top: 0; z-index: 1;
    width: 380px; height: 267px;
    background:
      linear-gradient(to right, var(--sign-white) 0%, rgba(255,255,255,0) 28%),
      radial-gradient(ellipse at 85% 70%, var(--photo-blue) 0%, rgba(156,200,234,0) 45%),
      radial-gradient(ellipse at 40% 55%, var(--photo-skin) 0%, rgba(232,201,176,0) 50%),
      var(--photo-light);
  }
  .brand-mark {
    position: absolute; left: 22px; top: 34px; z-index: 2;
    width: 150px; height: 130px;
    display: flex; align-items: center; justify-content: center;
    text-align: center;
    font-weight: 500; font-size: 21px; line-height: 1.2;
    color: var(--brand-blue);
  }
  .practice-name {
    position: absolute; left: 212px; top: 36px; z-index: 2;
    font-size: 30px; font-weight: 500; letter-spacing: 0.6px;
    color: var(--title-grey); white-space: nowrap;
  }
  .practice-type {
    position: absolute; left: 207px; top: 68px; z-index: 2;
    font-size: 47px; font-weight: 400; letter-spacing: -0.4px;
    color: var(--accent-pink); white-space: nowrap;
  }
  .phone {
    position: absolute; left: 232px; top: 136px; z-index: 2;
    display: flex; align-items: center; gap: 12px;
    font-size: 46px; font-weight: 500; color: var(--phone-blue);
    letter-spacing: 1px;
  }
  .phone-icon { width: 34px; height: 34px; margin-top: 8px; }
  .tagline-band {
    position: absolute; left: 0; top: 224px; z-index: 2;
    width: 660px; height: 33px;
    background: linear-gradient(to right, var(--band-green) 0%, var(--band-green) 90%, rgba(108,191,69,0) 100%);
  }
  .tagline {
    position: absolute; left: 86px; top: 3px;
    font-family: "Bitter", serif; font-weight: 300; font-size: 21px;
    color: var(--sign-white); letter-spacing: 0.4px; white-space: nowrap;
  }
</style>
</head>
<body>
  <section class="sign">
    <div class="hero-photo" role="img" aria-label="Photo of a nurse checking a smiling young boy with a stethoscope while his mother sits beside him"></div>

    <div class="brand-mark">Oakmere<br>Kin<br>Clinic</div>

    <h1 class="practice-name">BRENWICK KIN CLINIC</h1>
    <h2 class="practice-type">Medical Practice</h2>

    <p class="phone">
      <svg class="phone-icon" viewBox="0 0 24 24" aria-hidden="true">
        <path fill="#6cbf45" d="M6.6 10.8a15.1 15.1 0 0 0 6.6 6.6l2.2-2.2c.3-.3.7-.4 1-.2 1.1.4 2.3.6 3.6.6.6 0 1 .4 1 1V20c0 .6-.4 1-1 1A17 17 0 0 1 3 4c0-.6.4-1 1-1h3.5c.6 0 1 .4 1 1 0 1.3.2 2.5.6 3.6.1.3 0 .7-.2 1z"/>
      </svg>
      222 555 0148
    </p>

    <div class="tagline-band">
      <p class="tagline">Trustworthy Medical Care for all Patients</p>
    </div>
  </section>
</body>
</html>
```